tall cedar health and wellness group.

need a full website design , all information provided in word document labeled website blue print
Updates

Need extra days to review

Target Market(s)

first responders, military , people in crisis

Coding

Coded - Design and coding required

Number of Pages Required

1 page

```html
<!DOCTYPE html>
<html lang="en">
<head>
<meta charset="utf-8">
<title>Tall Cedar Health &amp; Wellness Group</title>
<link href="https://fonts.googleapis.com/css2?family=Roboto:wght@400;500;700;900&display=swap" rel="stylesheet">
<style>
:root{
  --blue:#1f5594;
  --blue-dark:#163f70;
  --navy:#0c1320;
  --ink:#1b1b1b;
  --text:#3c3c3c;
  --grey-bg:#f2f2f2;
  --grey-line:#9a9a9a;
  --white:#ffffff;
}
*{box-sizing:border-box;margin:0;padding:0}
html,body{width:1200px;height:4100px;overflow:hidden;background:var(--white);font-family:"Roboto",Arial,sans-serif;color:var(--text)}
.canvas{position:relative;width:1200px;height:4100px;overflow:hidden}
.abs{position:absolute}
.btn{position:absolute;background:var(--blue);color:var(--white);font-weight:700;font-size:14px;border-radius:24px;display:flex;align-items:center;justify-content:center;letter-spacing:.2px}
.section-title{position:absolute;font-weight:700;color:var(--ink);font-size:40px;letter-spacing:.5px}
.title-swash{position:absolute;height:10px}
.photo{position:absolute}

/* header */
.site-header{position:absolute;left:0;top:0;width:1200px;height:133px;background:var(--white);z-index:3}
.brand-badge{position:absolute;left:102px;top:-60px;width:248px;height:240px;border-radius:50%;background:var(--white);border-bottom:3px solid var(--blue);z-index:4}
.brand-mark{position:absolute;left:206px;top:28px;width:40px;height:40px;border-radius:50%;background:#9a9a9a;z-index:5}
.brand-name{position:absolute;left:102px;top:108px;width:248px;text-align:center;font-weight:700;color:var(--blue);font-size:20px;letter-spacing:.5px;z-index:5;line-height:1.15}
.brand-name small{display:block;font-size:9px;letter-spacing:.6px}
.phone{position:absolute;left:658px;top:26px;font-weight:700;font-size:17px;color:var(--ink);display:flex;align-items:center;gap:8px}
.nav{position:absolute;left:400px;top:88px;display:flex;gap:30px;font-size:13px;font-weight:700;color:var(--ink)}
.nav .active{color:var(--blue);position:relative}
.nav .active::after{content:"";position:absolute;left:0;top:20px;width:100%;height:3px;border-radius:3px;background:var(--blue)}
.nav-divider{position:absolute;left:913px;top:76px;width:1px;height:42px;background:#d8d8d8}
.social{position:absolute;width:32px;height:32px;border-radius:50%;border:1px solid #d8d8d8;background:var(--white)}
.social.fill{background:var(--blue);border-color:var(--blue)}

/* hero */
.hero-title{position:absolute;left:0;top:325px;width:1200px;text-align:center;color:var(--white);font-weight:700;font-size:42px;line-height:48px;text-shadow:0 2px 6px rgba(0,0,0,.35)}
.hero-sub{position:absolute;left:260px;top:428px;width:680px;text-align:center;color:var(--white);font-weight:500;font-size:17px;line-height:26px;text-shadow:0 1px 4px rgba(0,0,0,.5)}
.dot{position:absolute;top:644px;width:14px;height:14px;border-radius:50%;border:2px solid var(--white)}
.dot.on{background:var(--white)}

/* about */
.about-copy{position:absolute;left:145px;top:960px;width:432px;font-size:14px;line-height:24px;color:var(--text)}
.about-copy p+p{margin-top:8px}

/* services */
.services-band{position:absolute;left:0;top:1372px;width:1200px;height:648px;background:var(--grey-bg)}
.card{position:absolute;background:var(--white);border-radius:4px;box-shadow:0 4px 14px rgba(0,0,0,.08);text-align:center}
.card .card-img{position:absolute;left:7px;top:0;right:7px;height:193px;border-radius:4px}
.card h3{position:absolute;left:10px;right:10px;font-size:16px;font-weight:500;color:var(--ink);line-height:25px}
.card p{position:absolute;left:20px;right:20px;font-size:14px;line-height:24px;color:var(--text)}
.card a{position:absolute;left:0;right:0;font-size:13px;font-weight:700;color:var(--blue);text-decoration:underline}
.card.featured{border-bottom:4px solid var(--blue)}
.arrow-btn{position:absolute;width:34px;height:34px;border-radius:50%;display:flex;align-items:center;justify-content:center}

/* who we serve */
.serve-band{position:absolute;left:0;top:2020px;width:1200px;height:850px;background:linear-gradient(180deg,#1f5594 0%,#1b4d89 60%,#1d5290 100%)}
.serve-icon{position:absolute;width:74px;height:74px;border-radius:50%;border:2px solid rgba(255,255,255,.85);display:flex;align-items:center;justify-content:center}
.serve-icon.on{background:var(--white)}
.serve-label{position:absolute;color:var(--white);font-weight:700;font-size:14px;line-height:23px}
.serve-center{position:absolute;left:445px;top:2230px;width:310px;height:310px;border-radius:50%;background:var(--white);text-align:center}
.serve-center .mark{position:absolute;left:125px;top:70px;width:60px;height:60px;border-radius:50%;background:#9a9a9a}
.serve-center .name{position:absolute;left:0;top:150px;width:310px;font-weight:700;color:var(--blue);font-size:30px;line-height:1.1}
.serve-center .name small{display:block;font-size:10px;letter-spacing:1px;margin-top:4px}

/* partners */
.partner{position:absolute;top:3010px;width:206px;height:88px;background:var(--white);border-radius:4px;box-shadow:0 3px 14px rgba(0,0,0,.1);display:flex;align-items:center;justify-content:center}
.partner span{display:block;width:90px;height:36px;border-radius:6px;background:#c7c9cc}

/* contact */
.contact-photo{position:absolute;left:0;top:3210px;width:1200px;height:590px;background:linear-gradient(90deg,#e9dcd2 0%,#d8c4b6 20%,#ecebea 45%,#f4f4f4 60%,#f5f5f5 100%)}
.field-label{position:absolute;font-size:13px;color:var(--text)}
.field{position:absolute;background:var(--white);border:1px solid #e0e0e0;border-radius:3px}

/* footer */
.site-footer{position:absolute;left:0;top:3790px;width:1200px;height:310px;background:var(--navy)}
.footer-mark{position:absolute;left:215px;top:3875px;width:64px;height:64px;border-radius:50%;background:#b9bcc1}
.footer-name{position:absolute;left:150px;top:3960px;width:200px;text-align:center;color:#2e6fbf;font-weight:700;font-size:25px;line-height:1.1}
.footer-name small{display:block;font-size:9px;letter-spacing:.8px}
.foot-col{position:absolute;top:3843px;color:var(--white);font-size:13px}
.foot-col h4{font-size:14px;font-weight:700;margin-bottom:20px;letter-spacing:.3px}
.foot-col li{list-style:none;line-height:27px}
.contact-row{display:flex;gap:18px;align-items:flex-start;margin-bottom:16px;line-height:22px}
.contact-row i{display:inline-flex;width:22px;height:22px;border-radius:50%;background:#1b2436;align-items:center;justify-content:center;flex:none}
.foot-rule{position:absolute;left:145px;top:4045px;width:910px;height:1px;background:#2a3142}
.copyright{position:absolute;left:0;top:4060px;width:1200px;text-align:center;color:var(--white);font-size:12px}
.foot-social{position:absolute;top:4055px;width:32px;height:32px;border-radius:50%;background:var(--white)}
.foot-social.fill{background:var(--blue)}
</style>
</head>
<body>
<div class="canvas">

  <!-- Header -->
  <header class="site-header">
    <div class="phone">
      <svg width="14" height="14" viewBox="0 0 24 24"><path fill="#1f5594" d="M6.6 10.8a15 15 0 0 0 6.6 6.6l2.2-2.2a1 1 0 0 1 1-.25 11.4 11.4 0 0 0 3.6.6 1 1 0 0 1 1 1V20a1 1 0 0 1-1 1A17 17 0 0 1 3 4a1 1 0 0 1 1-1h3.5a1 1 0 0 1 1 1c0 1.25.2 2.45.6 3.6a1 1 0 0 1-.25 1z"/></svg>
      555 010 - 2048
    </div>
    <div class="btn" style="left:832px;top:14px;width:223px;height:44px;font-size:14px">BOOK A APPOINTMENT</div>
    <nav class="nav">
      <span class="active">HOME</span><span>ABOUT US</span><span>SERVICES</span><span>OUR TEAM</span><span>FAQ</span><span>CONTACT</span>
    </nav>
    <div class="nav-divider"></div>
    <div class="social" style="left:946px;top:82px"></div>
    <div class="social fill" style="left:984px;top:82px"></div>
    <div class="social" style="left:1022px;top:82px"></div>
  </header>
  <div class="brand-badge"></div>
  <div class="brand-mark"></div>
  <div class="brand-name">TALL CEDAR<small>HEALTH &amp; WELLNESS GROUP</small></div>

  <!-- Hero -->
  <div class="photo" role="img" aria-label="Police officer, firefighter and paramedic standing together in front of an ambulance" style="left:0;top:133px;width:1200px;height:670px;background:linear-gradient(90deg,#2b2f36 0%,#6a5b46 30%,#8a6c3d 50%,#5a4e44 70%,#2c3038 100%)"></div>
  <svg class="abs" style="left:0;top:640px" width="1200" height="170" viewBox="0 0 1200 170">
    <path d="M0 120 C200 30 380 20 600 95 C800 160 980 120 1200 10 L1200 170 L0 170Z" fill="#ffffff"/>
    <path d="M0 120 C200 30 380 20 600 95 C800 160 980 120 1200 10 L1200 30 C990 140 800 180 600 118 C380 50 200 60 0 150Z" fill="#1f5594"/>
  </svg>
  <h1 class="hero-title">HELPING THOSE WHO<br>HELP OTHERS</h1>
  <p class="hero-sub">A trauma-informed wellness centre dedicated to supporting first responders, frontline workers, and the communities they serve.</p>
  <div class="btn" style="left:488px;top:495px;width:224px;height:46px">EXPLORE OUR SERVICES</div>
  <span class="dot" style="left:566px"></span><span class="dot" style="left:592px"></span><span class="dot on" style="left:618px"></span>

  <!-- About -->
  <div class="abs" style="left:918px;top:818px;width:170px;height:170px;border-radius:50%;background:#eef1f5"></div>
  <h2 class="section-title" style="left:145px;top:876px">ABOUT US</h2>
  <svg class="title-swash" style="left:145px;top:925px" width="120" height="12" viewBox="0 0 120 12"><path d="M2 10 C40 -2 80 -2 118 8" stroke="#1f5594" stroke-width="4" fill="none" stroke-linecap="round"/></svg>
  <div class="about-copy">
    <p>Tall Cedar Health &amp; Wellness Group brings together mental health clinicians, rehabilitation professionals, and specialized wellness practitioners under one roof. Our team is committed to delivering compassionate, evidence-based care tailored to individuals who face high-stress, high-impact roles.</p>
    <p>Lorem ipsum dolor sit amet, consectetur adipiscing elit, sed do eiusmod tempor incididunt ut labore et dolore magna aliqua. Ut enim ad minim veniam, quisea.</p>
  </div>
  <div class="btn" style="left:145px;top:1188px;width:148px;height:46px">LEARN MORE</div>
  <div class="photo" role="img" aria-label="Smiling woman holding hands with a counsellor in a bright room" style="left:635px;top:850px;width:420px;height:420px;border-radius:50%;border:3px solid var(--blue);background:linear-gradient(135deg,#e8e4de 0%,#cbb9a6 45%,#e9e6e2 100%)"></div>

  <!-- Services -->
  <section class="services-band"></section>
  <h2 class="section-title" style="left:0;top:1444px;width:1200px;text-align:center">SERVICES OFFERED</h2>
  <svg class="title-swash" style="left:540px;top:1493px" width="120" height="12" viewBox="0 0 120 12"><path d="M2 10 C40 -2 80 -2 118 8" stroke="#1f5594" stroke-width="4" fill="none" stroke-linecap="round"/></svg>

  <div class="arrow-btn" style="left:80px;top:1667px;background:#dfe5ee">
    <svg width="16" height="10" viewBox="0 0 16 10"><path d="M15 5H2M6 1 2 5l4 4" stroke="#1f5594" stroke-width="2" fill="none"/></svg>
  </div>
  <div class="arrow-btn" style="left:1087px;top:1667px;background:var(--blue)">
    <svg width="16" height="10" viewBox="0 0 16 10"><path d="M1 5h13M10 1l4 4-4 4" stroke="#fff" stroke-width="2" fill="none"/></svg>
  </div>

  <div class="card" style="left:145px;top:1543px;width:282px;height:358px">
    <div class="card-img" role="img" aria-label="Therapist listening to a distressed client" style="background:linear-gradient(135deg,#6f7f8c,#c9c3bb 60%,#e4e0da)"></div>
    <h3 style="top:213px">MENTAL HEALTH THERAPY</h3>
    <p style="top:238px">Lorem ipsum dolor sit amet, consectetur adipiscing elit, sed do eiusmod tempor.</p>
    <a style="top:317px">LEARN MORE</a>
  </div>
  <div class="card featured" style="left:459px;top:1543px;width:282px;height:400px">
    <div class="card-img" role="img" aria-label="Two people holding hands in support" style="background:linear-gradient(135deg,#6e6a44,#c79a6e 55%,#e2c8a8)"></div>
    <h3 style="top:213px">TRAUMA &amp; FIRST<br>RESPONDER SUPPORT</h3>
    <p style="top:263px">Lorem ipsum dolor sit amet, consectetur adipiscing elit, sed do eiusmod tempor.</p>
    <a style="top:345px">LEARN MORE</a>
  </div>
  <div class="card" style="left:773px;top:1543px;width:283px;height:358px">
    <div class="card-img" role="img" aria-label="Occupational therapist working with an older patient" style="background:linear-gradient(135deg,#3d4a5c,#8a95a3 50%,#d9dde2)"></div>
    <h3 style="top:213px">OT &amp; REHABILITATION</h3>
    <p style="top:238px">Lorem ipsum dolor sit amet, consectetur adipiscing elit, sed do eiusmod tempor.</p>
    <a style="top:317px">LEARN MORE</a>
  </div>

  <!-- Who we serve -->
  <section class="serve-band" role="img" aria-label="Soft-focus background of a support session"></section>
  <h2 class="section-title" style="left:0;top:2080px;width:1200px;text-align:center;color:#fff">WHO WE SERVE</h2>
  <svg class="title-swash" style="left:540px;top:2128px" width="120" height="12" viewBox="0 0 120 12"><path d="M2 10 C40 -2 80 -2 118 8" stroke="#fff" stroke-width="4" fill="none" stroke-linecap="round"/></svg>

  <svg class="abs" style="left:400px;top:2200px" width="400" height="380" viewBox="0 0 400 380">
    <circle cx="200" cy="185" r="188" stroke="#ffffff" stroke-opacity=".7" stroke-width="2" fill="none"/>
    <g fill="#1f5594" stroke="#fff" stroke-width="2">
      <circle cx="76" cy="44" r="4"/><circle cx="324" cy="44" r="4"/><circle cx="12" cy="185" r="4"/>
      <circle cx="388" cy="185" r="4"/><circle cx="60" cy="326" r="4"/><circle cx="317" cy="330" r="4"/><circle cx="200" cy="373" r="4"/>
    </g>
  </svg>
  <div class="serve-center">
    <div class="mark"></div>
    <div class="name">TALL CEDAR<small>HEALTH &amp; WELLNESS GROUP</small></div>
  </div>

  <div class="serve-icon" style="left:396px;top:2173px"><svg width="34" height="34" viewBox="0 0 24 24" fill="none" stroke="#fff" stroke-width="1.4"><circle cx="12" cy="8" r="3"/><path d="M6 20c0-3.5 2.7-6 6-6s6 2.5 6 6"/></svg></div>
  <div class="serve-label" style="left:284px;top:2188px;text-align:right">FIRST<br>RESPONDERS</div>

  <div class="serve-icon" style="left:731px;top:2173px"><svg width="34" height="34" viewBox="0 0 24 24" fill="none" stroke="#fff" stroke-width="1.4"><circle cx="8" cy="9" r="2.5"/><circle cx="16" cy="9" r="2.5"/><path d="M3 19c0-3 2.2-5 5-5s5 2 5 5M11 19c0-3 2.2-5 5-5s5 2 5 5"/></svg></div>
  <div class="serve-label" style="left:817px;top:2188px">PUBLIC SAFETY<br>PERSONNEL</div>

  <div class="serve-icon on" style="left:323px;top:2348px"><svg width="34" height="34" viewBox="0 0 24 24" fill="none" stroke="#1f5594" stroke-width="1.4"><path d="M12 10.5c-1.5-2.2-4.5-1.2-4 1 .4 1.6 4 4 4 4s3.6-2.4 4-4c.5-2.2-2.5-3.2-4-1z"/><path d="M4 12v6l4 3M20 12v6l-4 3"/></svg></div>
  <div class="serve-label" style="left:130px;top:2361px;text-align:right">FRONTLINE /<br>HEALTHCARE WORKERS</div>

  <div class="serve-icon" style="left:803px;top:2348px"><svg width="34" height="34" viewBox="0 0 24 24" fill="none" stroke="#fff" stroke-width="1.4"><circle cx="9" cy="8" r="2.2"/><circle cx="15" cy="8" r="2.2"/><path d="M5 14h14M4 12v6l4 3M20 12v6l-4 3"/></svg></div>
  <div class="serve-label" style="left:890px;top:2361px">INDIVIDUALS,<br>COUPLES &amp; FAMILIES</div>

  <div class="serve-icon" style="left:415px;top:2535px"><svg width="34" height="34" viewBox="0 0 24 24" fill="none" stroke="#fff" stroke-width="1.4"><path d="M7 7h10l-1 3H8z"/><circle cx="12" cy="12" r="2.5"/><path d="M6 21c0-3.5 2.7-6 6-6s6 2.5 6 6"/></svg></div>
  <div class="serve-label" style="left:245px;top:2552px;text-align:right">VETERANS &amp;<br>MILITARY PERSONNEL</div>

  <div class="serve-icon" style="left:710px;top:2535px"><svg width="34" height="34" viewBox="0 0 24 24" fill="none" stroke="#fff" stroke-width="1.4"><circle cx="10" cy="9" r="3"/><path d="M3 15c3 1 6 3 8 3l8-3M13 6l2 2 4-4"/></svg></div>
  <div class="serve-label" style="left:796px;top:2552px">ORGANIZATIONS SEEKING WELLNESS<br>PARTNERSHIPS</div>

  <div class="serve-icon" style="left:562px;top:2588px"><svg width="34" height="34" viewBox="0 0 24 24" fill="none" stroke="#fff" stroke-width="1.4"><circle cx="12" cy="7" r="2.5"/><circle cx="7" cy="13" r="2"/><circle cx="17" cy="13" r="2"/><path d="M3 20c0-2.5 1.8-4 4-4s4 1.5 4 4M13 20c0-2.5 1.8-4 4-4s4 1.5 4 4"/></svg></div>
  <div class="serve-label" style="left:460px;top:2673px;width:280px;text-align:center">EMPLOYERS, AGENCIES &amp;<br>ORGANIZATIONS</div>

  <svg class="abs" style="left:0;top:2730px" width="1200" height="160" viewBox="0 0 1200 160">
    <path d="M0 110 C180 20 380 10 620 60 C850 110 1020 100 1200 10 L1200 160 L0 160Z" fill="#9a9a9a"/>
    <path d="M0 130 C180 45 380 30 620 80 C850 130 1020 120 1200 30 L1200 160 L0 160Z" fill="#ffffff"/>
  </svg>

  <!-- Partners -->
  <h2 class="section-title" style="left:0;top:2913px;width:1200px;text-align:center">OUR PARTNERS</h2>
  <svg class="title-swash" style="left:540px;top:2962px" width="120" height="12" viewBox="0 0 120 12"><path d="M2 10 C40 -2 80 -2 118 8" stroke="#1f5594" stroke-width="4" fill="none" stroke-linecap="round"/></svg>
  <div class="partner" style="left:145px"><span></span></div>
  <div class="partner" style="left:379px"><span></span></div>
  <div class="partner" style="left:614px"><span></span></div>
  <div class="partner" style="left:849px"><span></span></div>

  <!-- Contact -->
  <div class="contact-photo" role="img" aria-label="Thoughtful young woman seated on a sofa during a counselling session"></div>
  <h2 class="section-title" style="left:630px;top:3296px">CONTACT US</h2>
  <svg class="title-swash" style="left:630px;top:3344px" width="120" height="12" viewBox="0 0 120 12"><path d="M2 10 C40 -2 80 -2 118 8" stroke="#1f5594" stroke-width="4" fill="none" stroke-linecap="round"/></svg>
  <div class="field-label" style="left:630px;top:3375px">First Name</div>
  <div class="field-label" style="left:847px;top:3375px">Last Name</div>
  <div class="field" style="left:630px;top:3398px;width:209px;height:42px"></div>
  <div class="field" style="left:847px;top:3398px;width:209px;height:42px"></div>
  <div class="field-label" style="left:630px;top:3449px">Phone</div>
  <div class="field-label" style="left:847px;top:3449px">Email</div>
  <div class="field" style="left:630px;top:3472px;width:209px;height:42px"></div>
  <div class="field" style="left:847px;top:3472px;width:209px;height:42px"></div>
  <div class="field-label" style="left:630px;top:3522px">Message</div>
  <div class="field" style="left:630px;top:3545px;width:426px;height:67px"></div>
  <div class="btn" style="left:892px;top:3623px;width:164px;height:46px">SEND MESSAGE</div>

  <svg class="abs" style="left:0;top:3660px" width="1200" height="140" viewBox="0 0 1200 140">
    <path d="M0 115 C220 30 430 20 620 70 C820 120 1000 100 1200 40 L1200 140 L0 140Z" fill="#1f5594"/>
    <path d="M0 140 C220 55 430 45 620 95 C820 145 1000 125 1200 60 L1200 140Z" fill="#0c1320"/>
  </svg>

  <!-- Footer -->
  <footer class="site-footer"></footer>
  <div class="footer-mark"></div>
  <div class="footer-name">TALL CEDAR<small>HEALTH &amp; WELLNESS GROUP</small></div>
  <div class="foot-col" style="left:438px">
    <h4>QUICK LINKS</h4>
    <ul><li>Home</li><li>About Us</li><li>Services</li><li>Our Team</li><li>FAQ</li><li>Contact</li></ul>
  </div>
  <div class="foot-col" style="left:611px">
    <h4>QUICK LINKS</h4>
    <ul><li>Privacy Policy</li><li>Terms &amp; Conditions</li><li>Legal Support</li><li>Disclaimer</li></ul>
  </div>
  <div class="foot-col" style="left:795px;width:280px">
    <h4>CONTACT INFO</h4>
    <div class="contact-row"><i><svg width="10" height="10" viewBox="0 0 24 24"><path fill="#2e6fbf" d="M6.6 10.8a15 15 0 0 0 6.6 6.6l2.2-2.2a1 1 0 0 1 1-.25 11.4 11.4 0 0 0 3.6.6 1 1 0 0 1 1 1V20a1 1 0 0 1-1 1A17 17 0 0 1 3 4a1 1 0 0 1 1-1h3.5a1 1 0 0 1 1 1c0 1.25.2 2.45.6 3.6a1 1 0 0 1-.25 1z"/></svg></i>555 010 - 2048</div>
    <div class="contact-row"><i><svg width="10" height="10" viewBox="0 0 24 24"><path fill="#2e6fbf" d="M2 5h20v14H2zm2 2v.5l8 5 8-5V7z"/></svg></i>contact@tallcedarhealth.com</div>
    <div class="contact-row"><i><svg width="10" height="10" viewBox="0 0 24 24"><path fill="#2e6fbf" d="M12 2a7 7 0 0 0-7 7c0 5 7 13 7 13s7-8 7-13a7 7 0 0 0-7-7zm0 9.5A2.5 2.5 0 1 1 12 6.5a2.5 2.5 0 0 1 0 5z"/></svg></i>123, tall cedar health and wellness group<br>Northbrook, Ontario</div>
  </div>
  <div class="foot-rule"></div>
  <div class="copyright">© 2025 &nbsp;/&nbsp; All Rights Reserved</div>
  <div class="foot-social" style="left:945px"></div>
  <div class="foot-social fill" style="left:984px"></div>
  <div class="foot-social" style="left:1022px"></div>

</div>
</body>
</html>
```